Consulting firm needs elegant, modern designs

Business card design - I have a logo which has previously been developed for K-Pathways - I will attach. I will also attach specifications for the size of the business card.

We also need a logo design for our leadership consulting product - Frame of Guidance - we focus on improving workplace health by educating leaders and learning professionals about how the physical and emotional affects performance and engagement. I have some example logos and ideas which I will attach - these have attempted to bring in the body but I do not like the font (see www.frameofguidance.example for preferred font). Idea is to please have a 'body' visible somehow in the word Leadership, ensuring that this conveys flexibility and agility. Colors which I prefer are deep purple OR turquoise, together with silver. COLORS below are for LOGO design.

Target Market(s)

For the business card, it should be more masculine. The logo which will be attached should be neutralized into dark blue shades and silver. The business card K-Pathways is focused on business transformation - organizations who would require a consultant to help them enter new markets, for example.

Industry/Entity Type

Leadership

Contact Information for Business Card

Content:
K-Pathways
Molenkade 27
4921KT, Breda, The Netherlands
maarten@K-Pathways.example
www.K-Pathways.example

Colors for business card should be conservative and slightly more masculine. Use the K-Pathways logo but change the colors to blue or shades of gray/black.

Dimensions for cut
85 x 55 mm
1004 x 650 pixels
Full document size
88 x 58 mm
1040 x 685 pixels
For the best result, you need to design the full document size including the bleed

Logo Text

Frame of Guidance

Font styles to use
Serif
Sans Serif

Colors
876aae
333333
959595

Requirements
Must have
• Professional, modern and unique business card design
• Professional, elegant, and modern logo design - with creative thinking
Should not have
• Too many colors

```html
<!DOCTYPE html>
<html lang="en">
<head>
<meta charset="utf-8">
<title>K-Pathways Business Card</title>
<link rel="stylesheet" href="https://fonts.googleapis.com/css2?family=Source+Sans+3:wght@400;600&display=swap">
<style>
  :root {
    --backdrop: #2b2b2b;
    --card-dark: #242424;
    --card-light: #f4f4f4;
    --ink: #333333;
    --ink-soft: #555555;
    --accent: #23406a;
    --accent-soft: #3d5f8f;
    --silver: #b9bec6;
    --silver-dim: #6e737a;
  }
  * { margin: 0; padding: 0; box-sizing: border-box; }
  html, body {
    width: 1200px;
    height: 716px;
    overflow: hidden;
    background: var(--backdrop);
    font-family: "Source Sans 3", "Myriad Pro", sans-serif;
  }
  .stage {
    position: relative;
    width: 1200px;
    height: 716px;
  }
  .card {
    position: absolute;
    top: 190px;
    width: 520px;
    height: 336px;
    border-radius: 3px;
    box-shadow: 0 14px 30px rgba(0,0,0,0.45);
  }
  .card-front {
    left: 50px;
    background: var(--card-dark);
  }
  .card-back {
    left: 630px;
    background: var(--card-light);
  }

  /* Front */
  .front-brand {
    position: absolute;
    left: 0;
    right: 0;
    top: 118px;
    display: flex;
    align-items: center;
    justify-content: center;
    gap: 14px;
  }
  .brand-dot {
    width: 46px;
    height: 46px;
    border-radius: 50%;
    background: var(--accent-soft);
  }
  .front-name {
    font-size: 48px;
    font-weight: 600;
    color: var(--silver);
    letter-spacing: 0.5px;
  }
  .front-tagline {
    position: absolute;
    left: 0;
    right: 0;
    top: 190px;
    text-align: center;
    font-size: 17px;
    color: var(--silver-dim);
    letter-spacing: 0.4px;
  }

  /* Back */
  .back-brand {
    position: absolute;
    left: 40px;
    top: 138px;
    display: flex;
    align-items: center;
    gap: 10px;
  }
  .back-brand .brand-dot {
    width: 54px;
    height: 54px;
    background: var(--accent);
  }
  .back-name {
    font-size: 28px;
    font-weight: 600;
    color: var(--accent);
  }
  .contact {
    position: absolute;
    left: 268px;
    top: 86px;
  }
  .person-name {
    font-size: 25px;
    color: var(--ink);
    line-height: 1;
  }
  .person-title {
    font-size: 15px;
    color: var(--accent-soft);
    margin-top: 3px;
    margin-bottom: 14px;
  }
  .contact-list { list-style: none; }
  .contact-item {
    display: flex;
    align-items: flex-start;
    gap: 8px;
    font-size: 15px;
    color: var(--ink-soft);
    line-height: 20px;
    margin-bottom: 6px;
  }
  .contact-icon {
    flex: none;
    width: 20px;
    height: 20px;
    border-radius: 2px;
    background: var(--accent);
    display: flex;
    align-items: center;
    justify-content: center;
  }
  .contact-icon svg { width: 14px; height: 14px; }
</style>
</head>
<body>
<main class="stage">

  <section class="card card-front" aria-label="Business card front">
    <div class="front-brand">
      <span class="brand-dot"></span>
      <span class="front-name">K-Pathways</span>
    </div>
    <p class="front-tagline">Encouraging every step</p>
  </section>

  <section class="card card-back" aria-label="Business card back">
    <div class="back-brand">
      <span class="brand-dot"></span>
      <span class="back-name">K-Pathways</span>
    </div>

    <div class="contact">
      <p class="person-name">Your Name</p>
      <p class="person-title">Job title</p>
      <ul class="contact-list">
        <li class="contact-item">
          <span class="contact-icon">
            <svg viewBox="0 0 14 14"><path d="M2 5c0-2 2-3 5-3s5 1 5 3v1H9V5H5v1H2z M3 7h8l1 5H2z" fill="#fff"/></svg>
          </span>
          <span>000 000 0000</span>
        </li>
        <li class="contact-item">
          <span class="contact-icon">
            <svg viewBox="0 0 14 14"><rect x="1.5" y="3.5" width="11" height="7" fill="none" stroke="#fff"/><path d="M1.5 3.5L7 8l5.5-4.5" fill="none" stroke="#fff"/></svg>
          </span>
          <span>maarten@K-Pathways.example</span>
        </li>
        <li class="contact-item">
          <span class="contact-icon">
            <svg viewBox="0 0 14 14" fill="none" stroke="#fff"><circle cx="7" cy="7" r="5.5"/><ellipse cx="7" cy="7" rx="2.5" ry="5.5"/><path d="M1.5 7h11"/></svg>
          </span>
          <span>www.K-Pathways.example</span>
        </li>
        <li class="contact-item">
          <span class="contact-icon">
            <svg viewBox="0 0 14 14"><path d="M7 13S2.5 8 2.5 5.5a4.5 4.5 0 0 1 9 0C11.5 8 7 13 7 13z" fill="#fff"/><circle cx="7" cy="5.5" r="1.6" fill="#23406a"/></svg>
          </span>
          <span>Molenkade 27<br>4921KT, Breda, The Netherlands</span>
        </li>
      </ul>
    </div>
  </section>

</main>
</body>
</html>
```